looking for sleek business card to standout from the crowd!

We are a young biotechnology company looking to help you personalize your health through understanding your genetic make up. We need you help in making a clean but sleek business card design using our new logo. The goal? Any time we give our cards out, people say "nice card!" The feel we are going for is "modern-techy". We don't want to come across as an old, giant pharma company, but not trying to be a hipster either.

Target Market(s)

healthcare and biotechnology industry.

Industry/Entity Type

Biotechnology

Contact Information for Business Card

Info to include on the card will be NAME, TITLE, EMAIL, PHONE. The companies website (www.corvalinbio.com) should also be on the card some where. Would like the logo, when printed, to be raised.

Requirements
Must have
• The logo we have attached in the color it is in. Fonts for text should lean toward more professional/tech.
Nice to have
• Prefer white/light color background
Should not have
• cartoons, landscape backgrounds images.

```html
<!DOCTYPE html>
<html lang="en">
<head>
<meta charset="UTF-8">
<title>Corvalin Business Card</title>
<link href="https://fonts.googleapis.com/css2?family=Montserrat:wght@600;700&family=Open+Sans:wght@400;600&display=swap" rel="stylesheet">
<style>
  :root {
    --backdrop: #3a3330;
    --card-green: #72b35f;
    --card-light: #e4e5e6;
    --brand-blue: #1f7fd0;
    --brand-green: #8cc63f;
    --silver: #e9efe7;
    --ink: #4a4a4a;
  }
  * { margin: 0; padding: 0; box-sizing: border-box; }
  html, body { width: 1200px; height: 769px; overflow: hidden; background: var(--backdrop); }
  .canvas { position: relative; width: 1200px; height: 769px; }
  .card {
    position: absolute; top: 236px; width: 520px; height: 297px;
    box-shadow: 0 10px 30px rgba(0,0,0,.45); overflow: hidden;
  }
  .card-front { left: 50px; background: var(--card-green); }
  .card-back { left: 630px; background: var(--card-light); }

  .front-mark {
    position: absolute; left: 0; right: 0; top: 104px;
    display: flex; align-items: center; justify-content: center; gap: 12px;
  }
  .front-dot { width: 26px; height: 26px; border-radius: 50%; background: var(--silver); }
  .front-name {
    font-family: 'Montserrat', sans-serif; font-weight: 700; font-size: 34px;
    letter-spacing: 2px; color: var(--silver);
  }
  .front-url {
    position: absolute; left: 0; right: 0; top: 184px; text-align: center;
    font-family: 'Open Sans', sans-serif; font-size: 12px; letter-spacing: 5px; color: #f3f7f1;
  }

  .tab-left { position: absolute; left: 0; top: 48px; width: 8px; height: 92px; background: var(--brand-blue); border-radius: 0 6px 6px 0; }
  .tab-right { position: absolute; right: 0; top: 190px; width: 8px; height: 82px; background: var(--brand-green); border-radius: 6px 0 0 6px; }

  .holder { position: absolute; left: 40px; top: 48px; }
  .holder-name { font-family: 'Open Sans', sans-serif; font-weight: 600; font-size: 17px; color: var(--brand-blue); letter-spacing: .5px; }
  .holder-title { font-family: 'Open Sans', sans-serif; font-size: 13px; color: var(--brand-green); margin-top: -2px; }
  .contacts { list-style: none; margin-top: 10px; }
  .contacts li {
    display: flex; align-items: center; gap: 8px;
    font-family: 'Open Sans', sans-serif; font-size: 13px; color: var(--ink); line-height: 19px;
  }
  .contacts svg { width: 12px; height: 12px; fill: var(--brand-blue); flex: none; }

  .back-mark { position: absolute; right: 52px; top: 178px; display: flex; align-items: center; gap: 8px; }
  .back-name { font-family: 'Montserrat', sans-serif; font-weight: 700; font-size: 32px; color: var(--brand-blue); letter-spacing: 1px; }
  .back-dot { width: 30px; height: 30px; border-radius: 50%; background: var(--brand-green); }
</style>
</head>
<body>
<div class="canvas">
  <section class="card card-front">
    <div class="front-mark">
      <span class="front-dot"></span>
      <span class="front-name">CORVALIN</span>
    </div>
    <p class="front-url">www.corvalinbio.com</p>
  </section>

  <section class="card card-back">
    <span class="tab-left"></span>
    <span class="tab-right"></span>
    <div class="holder">
      <h1 class="holder-name">MARA ELLISON</h1>
      <p class="holder-title">CEO/Founder</p>
      <ul class="contacts">
        <li><svg viewBox="0 0 24 24"><path d="M6.6 10.8a15 15 0 0 0 6.6 6.6l2.2-2.2c.3-.3.7-.4 1-.2 1.1.4 2.3.6 3.6.6.6 0 1 .4 1 1V20c0 .6-.4 1-1 1A17 17 0 0 1 3 4c0-.6.4-1 1-1h3.5c.6 0 1 .4 1 1 0 1.3.2 2.5.6 3.6.1.3 0 .7-.2 1z"/></svg>555 014 2290</li>
        <li><svg viewBox="0 0 24 24"><path d="M2 5h20v14H2zM4 7v.5l8 5 8-5V7l-8 5z"/></svg>mellison@corvalinbio.com</li>
        <li><svg viewBox="0 0 24 24"><circle cx="12" cy="12" r="10"/></svg>www.corvalinbio.com</li>
      </ul>
    </div>
    <div class="back-mark">
      <span class="back-name">CORVALIN</span>
      <span class="back-dot"></span>
    </div>
  </section>
</div>
</body>
</html>
```